Dane Morrow films- wedding and event films company website. DESKTOP AND MOBILE

We need a website for a high-end wedding and event film production company. Looking for a very modern and elegant design. my old website is www.danemorrowfilms.example

I like the "white/black/rose gold" color scheme of my logo.

really looking for a sleek modern design the breaths professional and artistic.

Target Market(s)

wedding and event films.

Industry/Entity Type

Film Production

Number of Pages Required

5+ page

Colors

Designer to choose colors to be used in the design.

Requirements
Must have
• website name will be www.danemorrowfilms.example
• tagline is "CINEMATIC STORIES ABOUT YOU"
• sections: HOME, CONTACT, ABOUT, FILMS, BLOG
• You can see my old website at danemorrowfilms.example
• Website about section:
• Dane Morrow Films was Established with the basis of truly cinematic and artistic films in mind. Dane and his team routinely travel the globe documenting weddings and events for high profile clients and discerning couples. Dane was born and raised in Maui Hawaii and has a unique approach to his films that embody the essence of a Hollywood film. Dane has spent the last 10 years traveling the world documenting corporate events and weddings with multiple Award winning production companies. In 2017 Dane decided to establish his own brand “Dane Morrow films” that will take everything he has learned with his past experiences and push it to the next level. Aside from his personal achievements, Dane is extremely passionate about his craft and always looks forward to handcrafting beautiful wedding/event films for his clients. The style of work is non-traditional and the day of filming is extremely unobtrusive (as we are looking for natural-candid/ raw emotions).
• If you are looking for the best price in town, we are probably not the best option, but if you’re looking for the best quality and peace of mind on your wedding day, then you’re in the right place. Dane Morrow Films is a boutique studio that only accepts a limited number of assignments per year. Inquire early to ensure availability.
• LINKS TO VIMEO VIDEOS THAT WILL BE IN THE "FILMS' SECTION.
• BRENT FILM TRAILER - https://clipvault.example/508114362
• BRENT FEATURE FILM - https://clipvault.example/617392048
• JUNE AND ROB'S WEDDING - https://clipvault.example/724958160
• DRONE DEMO REEL - https://clipvault.example/841576203
• WEDDING INDUSTRY EVENT PARTY - https://clipvault.example/962304817/a8d3e7b21c
• images that you can use on site are here: https://brigittolsenimages.proofbox.example/gallery/nora&felix/
• password is: meadow

```html
<!DOCTYPE html>
<html lang="en">
<head>
<meta charset="utf-8">
<title>Dane Morrow Films — Cinematic Stories About You</title>
<link rel="stylesheet" href="https://fonts.googleapis.com/css2?family=Questrial&family=Didact+Gothic&display=swap">
<style>
:root{
  --rose:#c39069;
  --rose-dark:#b07e58;
  --blush:#f4eae8;
  --header-bg:#f7f0ef;
  --ink:#2d2b2a;
  --muted:#7b7572;
  --nav:#4b4644;
  --footer-bar:#2e2c2c;
  --white:#ffffff;
  --line:#d8cfcc;
}
*{box-sizing:border-box;margin:0;padding:0}
html,body{width:1200px;height:3209px;overflow:hidden}
body{position:relative;background:var(--white);font-family:"Questrial",sans-serif;color:var(--ink)}
.abs{position:absolute}
.btn{position:absolute;display:flex;align-items:center;justify-content:center;background:var(--rose);color:var(--white);border-radius:30px;font-family:"Questrial",sans-serif;text-transform:uppercase;letter-spacing:.5px}
.photo{position:absolute;overflow:hidden}
.photo .frame{position:absolute;inset:18px 18px 18px 18px;border:1px solid rgba(255,255,255,.75)}

/* header */
.site-header{position:absolute;left:0;top:0;width:1200px;height:122px;background:var(--header-bg)}
.contact-mini{position:absolute;left:205px;top:36px;font-size:15px;line-height:24px}
.contact-mini .phone{font-weight:bold;color:var(--ink)}
.contact-mini .mail{color:var(--muted);font-size:14px}
.contact-mini .ico{position:absolute;left:-38px;top:4px;width:22px;height:22px;border-radius:50%;background:var(--rose)}
.brand{position:absolute;left:500px;top:62px;width:200px;text-align:center;font-size:19px;letter-spacing:2px;color:var(--ink)}
.brand-mark{position:absolute;left:585px;top:20px;width:30px;height:30px;background:var(--rose)}
.book-btn{left:840px;top:38px;width:161px;height:48px;font-size:16px}

/* nav */
.main-nav{position:absolute;left:0;top:122px;width:1200px;height:50px;background:var(--nav)}
.main-nav a{position:absolute;top:15px;color:var(--white);font-size:16px;text-decoration:none}
.main-nav .sep{position:absolute;top:14px;width:1px;height:22px;background:rgba(255,255,255,.25)}

/* hero */
.hero{left:0;top:175px;width:1200px;height:645px;background:linear-gradient(100deg,#3d4a24 0%,#6b7a3a 30%,#9aa066 50%,#e8e2dc 62%,#273455 78%,#2f3b5e 100%)}
.hero-title{position:absolute;left:86px;top:395px;color:var(--white)}
.hero-title .small{font-size:45px;letter-spacing:1px;line-height:56px}
.hero-title .big{font-size:80px;line-height:92px;letter-spacing:1px}
.hero-rule{position:absolute;left:206px;top:580px;width:176px;height:1px;background:#d6b08b}
.hero-rule.second{top:588px}
.slider-dots span{position:absolute;left:1124px;width:16px;height:16px;border-radius:50%;border:2px solid var(--rose)}

/* promo */
.promo{position:absolute;left:0;top:826px;width:1200px;height:77px;background:var(--rose)}
.promo p{position:absolute;left:200px;top:24px;color:var(--white);font-size:25px;letter-spacing:.5px}
.promo .btn{left:826px;top:12px;width:186px;height:52px;background:var(--rose-dark);font-size:16px;box-shadow:0 1px 3px rgba(0,0,0,.15)}

/* section headings */
.section-title{position:absolute;left:0;width:1200px;text-align:center;font-size:43px;color:var(--ink)}
.divider{position:absolute;left:367px;width:466px;height:8px}
.divider::before,.divider::after{content:"";position:absolute;left:0;right:0;height:1px;background:var(--line)}
.divider::before{top:0}.divider::after{top:6px}
.divider span{position:absolute;left:198px;top:-7px;width:70px;height:20px;background:var(--white);border:1px solid var(--line);border-radius:10px}

/* plans */
.plan-photo{top:1114px;width:323px;height:204px}
.play{position:absolute;left:146px;top:87px;width:32px;height:32px;border-radius:50%;background:rgba(255,255,255,.55)}
.play::after{content:"";position:absolute;left:12px;top:9px;border-left:11px solid var(--white);border-top:7px solid transparent;border-bottom:7px solid transparent}
.plan-caption{position:absolute;top:1333px;width:323px;text-align:center;font-size:19px;color:var(--ink)}
.plan-btn{top:1367px;width:118px;height:38px;font-size:15px;text-transform:none}

/* about */
.about{position:absolute;left:0;top:1491px;width:1200px;height:535px;background:var(--blush)}
.about h2{position:absolute;left:86px;top:78px;font-size:40px;font-weight:normal}
.about .mini-rule{position:absolute;left:86px;top:155px;width:200px;height:1px;background:var(--line)}
.about p{position:absolute;left:86px;top:195px;width:535px;font-family:"Didact Gothic",sans-serif;font-size:14.2px;line-height:25.8px;color:var(--muted)}
.about .btn{left:86px;top:400px;width:151px;height:49px;font-size:17px;text-transform:none}
.about-photo{left:669px;top:77px;width:443px;height:381px;background:linear-gradient(90deg,#e9eae4 0%,#c9cbbf 25%,#5a6844 45%,#2a3552 75%,#1d2438 100%)}
.about-arrows{position:absolute;left:294px;top:299px;width:121px;height:56px;background:var(--rose)}
.about-arrows i{position:absolute;top:14px;width:28px;height:28px;border:2px solid var(--white);border-radius:50%}

/* blog */
.blog-photo{top:2233px;width:323px;height:205px}
.date-tag{position:absolute;left:100px;top:150px;width:123px;height:37px;background:rgba(195,144,105,.9);color:var(--white);font-size:15px;text-align:center;line-height:37px}
.blog-meta{position:absolute;top:2451px;width:323px;text-align:center;font-size:12.5px;color:var(--muted)}
.blog-title{position:absolute;top:2483px;width:323px;text-align:center;font-size:19px;line-height:30px;color:var(--ink)}

/* testimonial */
.testimonial{position:absolute;left:86px;top:2672px;width:1028px;height:207px;background:var(--rose)}
.avatar{left:531px;top:-60px;width:138px;height:138px;border-radius:50%;border:4px solid var(--white);background:radial-gradient(circle at 50% 45%,#e8c9a4 0%,#c89a6a 55%,#8d6a4d 100%)}
.testimonial .quote{position:absolute;left:0;top:102px;width:1028px;text-align:center;color:var(--white);font-size:20px}
.testimonial .who{position:absolute;left:0;top:145px;width:1028px;text-align:center;color:#f1dcc8;font-size:17px}
.t-arrow{position:absolute;top:106px;width:30px;height:30px;border:1px solid rgba(255,255,255,.6);border-radius:50%}

/* footer */
.footer-brand{position:absolute;left:137px;top:2960px;font-size:19px;letter-spacing:2px;color:var(--ink)}
.footer-mark{position:absolute;left:240px;top:2908px;width:36px;height:36px;background:var(--rose)}
.footer-phone{position:absolute;left:152px;top:3020px;font-size:14px;font-weight:bold}
.socials span{position:absolute;top:3069px;width:27px;height:27px;border-radius:50%;background:var(--rose)}
.footer-col-title{position:absolute;top:2932px;font-size:14px;color:var(--ink)}
.footer-sep{position:absolute;top:2925px;width:1px;height:180px;background:var(--line)}
.quick-links li{position:absolute;left:406px;list-style:none;font-size:12px;color:var(--ink)}
.quick-links li::before{content:"→";color:var(--rose);margin-right:12px}
.thumb{position:absolute;width:46px;height:36px;background:linear-gradient(135deg,#c7845c,#4a5f8a)}
.field{position:absolute;left:862px;width:201px;height:34px;border:1px solid var(--line);background:var(--white);font-size:11px;color:var(--muted);padding:10px 8px}
.submit{position:absolute;left:862px;top:3061px;width:201px;height:32px;background:var(--rose);color:var(--white);font-size:11px;text-align:center;line-height:32px}
.footer-bar{position:absolute;left:0;top:3151px;width:1200px;height:58px;background:var(--footer-bar);color:#d8d2cf;font-size:12px;text-align:center;line-height:58px}
</style>
</head>
<body>

<header class="site-header">
  <div class="contact-mini">
    <span class="ico"></span>
    <div class="phone">(808) 555-0148</div>
    <div class="mail">dane@danemorrowfilms.example</div>
  </div>
  <span class="brand-mark"></span>
  <div class="brand">DANE MORROW FILMS</div>
  <a class="btn book-btn">Book now</a>
</header>

<nav class="main-nav">
  <a style="left:199px">Home</a><span class="sep" style="left:300px"></span>
  <a style="left:366px">Contact</a><span class="sep" style="left:480px"></span>
  <a style="left:542px">About</a><span class="sep" style="left:644px"></span>
  <a style="left:704px">Films</a><span class="sep" style="left:800px"></span>
  <a style="left:854px">Blog</a>
  <svg class="abs" style="left:980px;top:16px" width="18" height="18" viewBox="0 0 18 18"><circle cx="7.5" cy="7.5" r="5.5" fill="none" stroke="#8d8684" stroke-width="1.6"/><line x1="11.5" y1="11.5" x2="16" y2="16" stroke="#8d8684" stroke-width="1.6"/></svg>
</nav>

<section>
  <div class="photo hero" role="img" aria-label="Wedding couple embracing outdoors, bride in white and groom in navy suit, greenery behind"></div>
  <h1 class="hero-title"><div class="small">CINEMATIC STORIES</div><div class="big">ABOUT YOU</div></h1>
  <span class="hero-rule"></span><span class="hero-rule second"></span>
  <div class="slider-dots">
    <span style="top:462px"></span>
    <span style="top:487px;background:var(--rose)"></span>
    <span style="top:512px"></span>
    <span style="top:537px"></span>
  </div>
</section>

<section class="promo">
  <p>ORDER FULL PACKAGE PLAN &amp; GET -25% DISCOUNT!</p>
  <a class="btn">Order now</a>
</section>

<section class="plans">
  <h2 class="section-title" style="top:968px;font-weight:normal">Perfect Wedding plans</h2>
  <div class="divider" style="top:1050px"><span></span></div>

  <div class="photo plan-photo" style="left:86px;background:linear-gradient(90deg,#3a7fc4 0%,#6fa6dc 40%,#e6ecf2 60%,#1d2a4a 85%,#2c6a3a 100%)" role="img" aria-label="Couple posing by the sea under a blue sky"><span class="frame"></span><span class="play"></span></div>
  <div class="photo plan-photo" style="left:438px;background:linear-gradient(160deg,#6b8a4e 0%,#a5ab84 45%,#cfd1c6 70%,#7d776c 100%)" role="img" aria-label="Groom lifting bride on a rocky coastal path"><span class="frame"></span><span class="play"></span></div>
  <div class="photo plan-photo" style="left:791px;background:linear-gradient(170deg,#8f8a78 0%,#b7b3a3 45%,#e2dfd6 70%,#6f6c64 100%)" role="img" aria-label="Couple walking together along rocky cliffs"><span class="frame"></span><span class="play"></span></div>

  <p class="plan-caption" style="left:86px">Lorem Ipsum is simply dummy text</p>
  <p class="plan-caption" style="left:438px">Lorem Ipsum is simply dummy text</p>
  <p class="plan-caption" style="left:791px">Lorem Ipsum is simply dummy text</p>
  <a class="btn plan-btn" style="left:189px">order now</a>
  <a class="btn plan-btn" style="left:541px">order now</a>
  <a class="btn plan-btn" style="left:894px">order now</a>
</section>

<section class="about">
  <h2>About Dane Morrow Films</h2>
  <span class="mini-rule"></span>
  <p>Dane Morrow Films was Established with the basis of truly cinematic and artistic films in mind. Dane and his team routinely travel the globe documenting weddings and events for high profile clients and discerning couples. Dane was born and raised in Maui Hawaii and has a unique approach to his films that embody the essence of a Hollywood film. Dane has spent the last 10 years traveling the world documenting corporate events and weddings with multiple Award winning production companies.</p>
  <a class="btn">Read More</a>
  <div class="photo about-photo" role="img" aria-label="Bride and groom reading vows beside white calla lilies">
    <span class="frame"></span>
    <div class="about-arrows">
      <i style="left:18px"></i><i style="left:72px"></i>
      <svg class="abs" style="left:26px;top:22px" width="14" height="14" viewBox="0 0 14 14"><path d="M9 2 L4 7 L9 12" fill="none" stroke="#fff" stroke-width="2"/></svg>
      <svg class="abs" style="left:81px;top:22px" width="14" height="14" viewBox="0 0 14 14"><path d="M5 2 L10 7 L5 12" fill="none" stroke="#fff" stroke-width="2"/></svg>
    </div>
  </div>
</section>

<section class="blogs">
  <h2 class="section-title" style="top:2094px;font-weight:normal">Our recent Blogs</h2>
  <div class="divider" style="top:2180px"><span></span></div>

  <div class="photo blog-photo" style="left:86px;background:linear-gradient(120deg,#5a1e0c 0%,#c2551c 40%,#f0a050 60%,#3a1608 100%)" role="img" aria-label="Champagne bottles on a warmly lit reception table"><span class="frame"></span><span class="date-tag">Jul 27, 2016</span></div>
  <div class="photo blog-photo" style="left:438px;background:linear-gradient(90deg,#1e4fa8 0%,#e9edf4 35%,#2a2a2a 60%,#2558b8 100%)" role="img" aria-label="Guests seated at a wedding reception table with blue backdrop"><span class="frame"></span><span class="date-tag">Jul 27, 2016</span></div>
  <div class="photo blog-photo" style="left:791px;background:linear-gradient(100deg,#d9c9b0 0%,#f3ece0 40%,#38405a 60%,#e8e4dc 100%)" role="img" aria-label="Celebrating guests in a bright banquet hall with white flowers"><span class="frame"></span><span class="date-tag">Jul 27, 2016</span></div>

  <p class="blog-meta" style="left:86px">By Mara Whitlow &nbsp;&nbsp;|&nbsp;&nbsp; 3 comments</p>
  <p class="blog-meta" style="left:438px">By Mara Whitlow &nbsp;&nbsp;|&nbsp;&nbsp; 3 comments</p>
  <p class="blog-meta" style="left:791px">By Mara Whitlow &nbsp;&nbsp;|&nbsp;&nbsp; 3 comments</p>
  <h3 class="blog-title" style="left:86px;font-weight:normal">An occasion that joins two hearts<br>in a symphony</h3>
  <h3 class="blog-title" style="left:438px;font-weight:normal">An occasion that joins two hearts<br>in a symphony</h3>
  <h3 class="blog-title" style="left:791px;font-weight:normal">An occasion that joins two hearts<br>in a symphony</h3>
</section>

<section class="testimonial">
  <div class="photo avatar" role="img" aria-label="Portrait of the reviewing bride"></div>
  <span class="t-arrow" style="left:36px"></span>
  <span class="t-arrow" style="left:962px"></span>
  <svg class="abs" style="left:44px;top:114px" width="14" height="14" viewBox="0 0 14 14"><path d="M9 2 L4 7 L9 12" fill="none" stroke="#fff" stroke-width="1.5"/></svg>
  <svg class="abs" style="left:971px;top:114px" width="14" height="14" viewBox="0 0 14 14"><path d="M5 2 L10 7 L5 12" fill="none" stroke="#fff" stroke-width="1.5"/></svg>
  <p class="quote">Dane really is one of the best film makers in Hawaii, great work Dane! We loved the film</p>
  <p class="who">Lena Barrow, Bride</p>
</section>

<footer>
  <span class="footer-mark"></span>
  <div class="footer-brand">DANE MORROW FILMS</div>
  <svg class="abs" style="left:130px;top:3021px" width="14" height="14" viewBox="0 0 24 24"><path d="M6.6 10.8a15 15 0 006.6 6.6l2.2-2.2a1 1 0 011-.25 11.4 11.4 0 003.6.57 1 1 0 011 1V20a1 1 0 01-1 1A17 17 0 013 4a1 1 0 011-1h3.5a1 1 0 011 1c0 1.25.2 2.45.57 3.57a1 1 0 01-.25 1z" fill="#c39069"/></svg>
  <div class="footer-phone">(808) 555-0148</div>
  <div class="socials">
    <span style="left:136px"></span><span style="left:178px"></span><span style="left:224px"></span><span style="left:268px"></span>
  </div>

  <span class="footer-sep" style="left:340px"></span>
  <span class="footer-sep" style="left:810px"></span>

  <h4 class="footer-col-title" style="left:406px;font-weight:normal">Quick Links</h4>
  <ul class="quick-links">
    <li style="top:2980px">Home</li>
    <li style="top:3006px">Contact</li>
    <li style="top:3032px">About</li>
    <li style="top:3058px">Films</li>
    <li style="top:3084px">Blog</li>
  </ul>

  <h4 class="footer-col-title" style="left:586px;font-weight:normal">Recent Gallery</h4>
  <div class="gallery">
    <span class="thumb" style="left:582px;top:2966px"></span><span class="thumb" style="left:640px;top:2966px"></span><span class="thumb" style="left:698px;top:2966px"></span>
    <span class="thumb" style="left:582px;top:3012px"></span><span class="thumb" style="left:640px;top:3012px"></span><span class="thumb" style="left:698px;top:3012px"></span>
    <span class="thumb" style="left:582px;top:3058px"></span><span class="thumb" style="left:640px;top:3058px"></span><span class="thumb" style="left:698px;top:3058px"></span>
  </div>

  <h4 class="footer-col-title" style="left:862px;font-weight:normal">Contact Us</h4>
  <div class="field" style="top:2971px">Name...</div>
  <div class="field" style="top:3016px">Email...</div>
  <div class="submit">SUBMIT</div>

  <div class="footer-bar">danemorrowfilms.example 2017. All rights reserved</div>
</footer>

</body>
</html>
```